Create a business promotion flyer to leave in customer mailboxes. We are a bulk petroleum supplier, servicing any industry that requires diesel. Base in griffith NSW, servicing griffith area and surrounds.

Business Name - Terra Petro
Fuel@terrapetro-example.com.au
Marco - 0400 000 001 mtorrisi@terrapetro-example.com.au
Liam - 0400 000 002 lharcourt@terrapetro-example.com.au
Peter - 0400 000 003 pwinslow@terrapetro-example.com.au
Office 02 5550 0100

Bulk Fuel deliveries.
Oils & lubricants
Local Family owned business

```html
<!DOCTYPE html>
<html lang="en">
<head>
<meta charset="utf-8">
<title>Terra Petro – Bulk Fuel Flyer</title>
<link href="https://fonts.googleapis.com/css2?family=Barlow+Condensed:wght@500;600;700;800&family=Source+Sans+3:wght@400;600&family=Dancing+Script:wght@400&display=swap" rel="stylesheet">
<style>
  :root{
    --paper:#f1efec;
    --ink:#111111;
    --charcoal:#3a3a3a;
    --red:#c8231f;
    --red-deep:#b81f1b;
    --rule:#bdbab5;
    --white:#ffffff;
    --cond:"Barlow Condensed", "Arial Narrow", sans-serif;
    --body:"Source Sans 3", Arial, sans-serif;
    --script:"Dancing Script", cursive;
  }
  *{margin:0;padding:0;box-sizing:border-box}
  html,body{width:800px;height:1200px;overflow:hidden;background:var(--paper)}
  .flyer{position:relative;width:800px;height:1200px;background:var(--paper);color:var(--ink);font-family:var(--body);overflow:hidden}

  /* Header */
  .brand{position:absolute;left:52px;top:72px;display:flex;align-items:center;gap:12px}
  .brand-mark{width:30px;height:30px;background:var(--red)}
  .brand-name{font-family:var(--cond);font-weight:700;font-size:54px;color:var(--red);line-height:1;white-space:nowrap}
  .header-divider{position:absolute;left:341px;top:27px;width:1px;height:157px;background:var(--charcoal)}
  .headline{position:absolute;left:366px;top:18px;font-family:var(--cond);font-weight:700;line-height:.95;text-transform:uppercase;white-space:nowrap}
  .headline .line-1{display:block;font-size:72px;color:var(--ink)}
  .headline .line-2{display:block;font-size:72px;color:var(--red);letter-spacing:-.3px}
  .tagline{position:absolute;left:372px;top:160px;font-family:var(--cond);font-weight:600;font-size:21px;color:var(--ink);white-space:nowrap}

  /* Hero */
  .hero{position:absolute;left:0;top:197px;width:800px;height:309px;
    background:linear-gradient(180deg,#6f9fce 0%,#b9d0e6 38%,#e9edf0 52%,#d9d9d6 62%,#8d7b63 82%,#6b5a45 100%)}

  /* Services */
  .services{position:absolute;left:0;top:506px;width:800px;height:228px;display:flex}
  .service{flex:1;text-align:center;padding-top:16px;position:relative}
  .service + .service::before{content:"";position:absolute;left:0;top:22px;height:196px;width:1px;background:var(--rule)}
  .service svg{width:54px;height:56px;stroke:var(--red);fill:none;stroke-width:2.4}
  .service-title{margin-top:10px;font-family:var(--cond);font-weight:700;font-size:21px;line-height:1.05;text-transform:uppercase}
  .service-text{margin-top:8px;font-size:14px;line-height:1.35;color:#222}

  /* Region band */
  .region{position:absolute;left:0;top:738px;width:800px;height:205px}
  .region svg.band{position:absolute;inset:0}
  .region-copy{position:absolute;left:74px;top:32px;color:var(--white)}
  .region-title{font-family:var(--cond);font-weight:700;font-size:27px;line-height:1.02;text-transform:uppercase}
  .region-rule{width:48px;height:2px;background:var(--red);margin:8px 0 8px}
  .region-text{font-size:16.5px;line-height:1.4;color:#ececec}

  .stamp{position:absolute;left:543px;top:764px;width:180px;height:180px}
  .stamp-text{font-family:var(--cond);font-weight:800;fill:var(--ink)}

  /* Contact */
  .contact{position:absolute;left:56px;top:955px;width:436px}
  .contact-title{font-family:var(--cond);font-weight:700;font-size:28px;line-height:1}
  .contact-sub{font-family:var(--cond);font-weight:700;font-size:17px;color:var(--red);margin-top:4px}
  .contact-list{list-style:none;margin-top:10px;width:400px}
  .contact-row{display:flex;align-items:center;height:29px;border-bottom:1px dotted var(--rule);font-size:13.5px;white-space:nowrap}
  .contact-row:last-child{border-bottom:none}
  .contact-row svg{width:16px;height:16px;fill:var(--ink);margin-right:13px;flex:none}
  .contact-name{font-weight:600;width:79px;font-size:14.5px}
  .contact-phone{width:133px}
  .contact-email{font-size:12px}

  .promise{position:absolute;left:493px;top:969px;width:307px;height:169px;background:var(--red-deep);color:var(--white);padding:18px 0 0 68px}
  .promise-script{font-family:var(--script);font-size:29px;line-height:1.3}
  .promise-call{font-family:var(--cond);font-weight:700;font-size:18px;line-height:1.1;margin-top:12px;text-transform:uppercase}

  /* Values strip */
  .values{position:absolute;left:52px;top:1138px;width:700px;height:62px;border-top:1px solid var(--rule);display:flex}
  .value{flex:1;display:flex;align-items:flex-start;gap:12px;padding:8px 0 0 2px;position:relative}
  .value + .value{padding-left:36px}
  .value + .value::before{content:"";position:absolute;left:0;top:14px;height:44px;width:1px;background:var(--rule)}
  .value svg{width:34px;height:40px;stroke:var(--ink);fill:none;stroke-width:2.2;flex:none}
  .value-title{font-family:var(--cond);font-weight:700;font-size:15px;line-height:1.1}
  .value-text{font-size:12px;line-height:1.2;color:#222}
</style>
</head>
<body>
<main class="flyer">

  <header>
    <div class="brand"><span class="brand-mark"></span><span class="brand-name">Terra Petro</span></div>
    <div class="header-divider"></div>
    <h1 class="headline"><span class="line-1">Fueling</span><span class="line-2">Your Business</span></h1>
    <p class="tagline">RELIABLE. LOCAL. READY TO DELIVER.</p>
  </header>

  <div class="hero" role="img" aria-label="Photo of a white Terra Petro road train fuel tanker parked on a dirt yard in front of grain silos under a blue sky"></div>

  <section class="services">
    <div class="service">
      <svg viewBox="0 0 56 58"><rect x="8" y="6" width="26" height="44" rx="4"/><rect x="13" y="12" width="16" height="11" rx="2"/><circle cx="21" cy="35" r="4"/><path d="M4 52h34"/><path d="M34 20l9 6v18a3 3 0 0 0 6 0V22l-6-8"/></svg>
      <h2 class="service-title">Bulk Fuel<br>Deliveries</h2>
      <p class="service-text">Reliable on-time<br>deliveries of<br>premium diesel.</p>
    </div>
    <div class="service">
      <svg viewBox="0 0 56 58"><path d="M28 5C22 16 11 27 11 38a17 17 0 0 0 34 0C45 27 34 16 28 5z"/><path d="M19 38a9 9 0 0 0 9 9"/></svg>
      <h2 class="service-title">Oils &amp;<br>Lubricants</h2>
      <p class="service-text">Quality products<br>to keep your<br>equipment<br>performing.</p>
    </div>
    <div class="service">
      <svg viewBox="0 0 70 58"><circle cx="35" cy="17" r="11"/><path d="M15 52c0-13 9-21 20-21s20 8 20 21z"/><circle cx="16" cy="20" r="7"/><path d="M4 46c0-9 5-14 11-15"/><circle cx="54" cy="20" r="7"/><path d="M66 46c0-9-5-14-11-15"/></svg>
      <h2 class="service-title">Local. Family<br>Owned.</h2>
      <p class="service-text">Proudly local,<br>personally committed<br>to our community<br>and customers.</p>
    </div>
  </section>

  <section class="region">
    <svg class="band" viewBox="0 0 800 205" preserveAspectRatio="none">
      <path d="M0 6 L60 0 L300 8 L520 2 L800 10 L792 40 L800 80 L795 150 L780 188 L500 184 L300 190 L40 194 L10 170 L2 120 L8 60 Z" fill="#121212"/>
      <path d="M12 178 L300 168 L640 172 L720 182 L700 196 L300 198 L18 200 Z" fill="#2f2f2f"/>
      <path d="M14 178 L250 170 L420 174 L300 186 L16 196 Z" fill="#a31c18"/>
    </svg>
    <div class="region-copy">
      <h2 class="region-title">Servicing Griffith<br>&amp; Surrounds</h2>
      <div class="region-rule"></div>
      <p class="region-text">Proudly supporting local industries,<br>farms, transport, construction,<br>manufacturing &amp; more.</p>
    </div>
  </section>

  <svg class="stamp" viewBox="0 0 180 180" aria-label="Local family owned business">
    <defs>
      <path id="arc-top" d="M30 90 A60 60 0 0 1 150 90"/>
      <path id="arc-bottom" d="M22 90 A68 68 0 0 0 158 90"/>
    </defs>
    <circle cx="90" cy="90" r="88" fill="#ffffff"/>
    <circle cx="90" cy="90" r="84" fill="none" stroke="#111" stroke-width="3"/>
    <circle cx="90" cy="90" r="78" fill="none" stroke="#111" stroke-width="1.2"/>
    <text class="stamp-text" font-size="22"><textPath href="#arc-top" startOffset="50%" text-anchor="middle">LOCAL</textPath></text>
    <text class="stamp-text" font-size="18"><textPath href="#arc-bottom" startOffset="50%" text-anchor="middle">BUSINESS</textPath></text>
    <path d="M52 58 Q90 46 128 58 M52 122 Q90 134 128 122" fill="none" stroke="#111" stroke-width="1"/>
    <g fill="#c8231f"><circle cx="78" cy="52" r="2.5"/><circle cx="90" cy="49" r="4"/><circle cx="102" cy="52" r="2.5"/><circle cx="78" cy="128" r="2.5"/><circle cx="90" cy="131" r="4"/><circle cx="102" cy="128" r="2.5"/></g>
    <text class="stamp-text" x="90" y="87" font-size="33" text-anchor="middle">FAMILY</text>
    <text class="stamp-text" x="90" y="117" font-size="33" text-anchor="middle">OWNED</text>
  </svg>

  <section class="contact">
    <h2 class="contact-title">CONTACT OUR TEAM</h2>
    <p class="contact-sub">WE’RE HERE TO HELP.</p>
    <ul class="contact-list">
      <li class="contact-row"><svg viewBox="0 0 16 16"><circle cx="8" cy="4.5" r="3.5"/><path d="M1 16c0-4 3-6.5 7-6.5s7 2.5 7 6.5z"/></svg><span class="contact-name">Marco</span><span class="contact-phone">0400 000 001</span><span class="contact-email">mtorrisi@terrapetro-example.com.au</span></li>
      <li class="contact-row"><svg viewBox="0 0 16 16"><circle cx="8" cy="4.5" r="3.5"/><path d="M1 16c0-4 3-6.5 7-6.5s7 2.5 7 6.5z"/></svg><span class="contact-name">Liam</span><span class="contact-phone">0400 000 002</span><span class="contact-email">lharcourt@terrapetro-example.com.au</span></li>
      <li class="contact-row"><svg viewBox="0 0 16 16"><circle cx="8" cy="4.5" r="3.5"/><path d="M1 16c0-4 3-6.5 7-6.5s7 2.5 7 6.5z"/></svg><span class="contact-name">Peter</span><span class="contact-phone">0400 000 003</span><span class="contact-email">pwinslow@terrapetro-example.com.au</span></li>
      <li class="contact-row"><svg viewBox="0 0 16 16"><path d="M3.5 1l3 3-1.8 2.2a9 9 0 0 0 5 5L12 9.5l3 3-2 2.5C7 15 1 9 1 3z"/></svg><span class="contact-name">Office</span><span class="contact-phone">02 5550 0100</span><span class="contact-email">Fuel@terrapetro-example.com.au</span></li>
    </ul>
  </section>

  <aside class="promise">
    <p class="promise-script">Locally owned.<br>Locally invested.</p>
    <p class="promise-call">Fueling<br>our community.</p>
  </aside>

  <footer class="values">
    <div class="value">
      <svg viewBox="0 0 34 40"><path d="M17 3 L31 8 V20 C31 29 24 35 17 38 C10 35 3 29 3 20 V8 Z"/><path d="M10 20l5 5 9-10"/></svg>
      <div><p class="value-title">RELIABLE</p><p class="value-text">You can<br>count on us.</p></div>
    </div>
    <div class="value">
      <svg viewBox="0 0 34 40"><circle cx="17" cy="20" r="15"/><path d="M17 10v10l7 5"/></svg>
      <div><p class="value-title">ON TIME</p><p class="value-text">When you<br>need it.</p></div>
    </div>
    <div class="value">
      <svg viewBox="0 0 34 40"><path d="M17 4C13 12 6 19 6 27a11 11 0 0 0 22 0C28 19 21 12 17 4z"/><path d="M11 27a6 6 0 0 0 6 6"/></svg>
      <div><p class="value-title">QUALITY</p><p class="value-text">Fuel you can<br>trust.</p></div>
    </div>
    <div class="value">
      <svg viewBox="0 0 34 40"><path d="M17 38C9 28 5 21 5 15a12 12 0 0 1 24 0c0 6-4 13-12 23z"/><circle cx="17" cy="15" r="5"/></svg>
      <div><p class="value-title">LOCAL</p><p class="value-text">Proudly<br>Griffith.</p></div>
    </div>
  </footer>

</main>
</body>
</html>
```